Indonesian B2B Company (Varo Ingredients) - Stationery Design

Varo Ingredients needs a corporate, bold and professional-looking stationery design.

Varo Ingredients is a new Indonesian company manufacturing, marketing and distributing various ingredients / raw materials such as flavours, fragrance, colours, sweeteners, preservatives for the food & beverage, pharmaceutical, personal care and other household goods industries.

It is a business to business (B2B) company as we supply various natural and synthetic raw materials to various consumer goods manufacturers. We therefore need a logo/identity with corporate and industrial style.

Varo Ingredients is a startup company which belongs to a larger Varo Tunggal group of companies (http://varotunggal.dealpathway.com/about) that focuses in the mining, petroleum and energy businesses. Varo Ingredients would like to focus in providing good quality, safe, reliable and affordable ingredients for the industries. Our tagline is "Ingredients for Your Success"
Updates

We have updated some information including our requirements and contact details to be shown in the stationery. Please check the project brief.

Regards,

Varo Ingredients

Target Market(s)

Manufacturers of food & beverages, personal care, pharmaceutical and other FMCG factories.

Industry/Entity Type

Business

Requirements
Must have
• Smart, professional and corporate touches in the stationery designs. We require designs for:
1. Letterhead
2. Envelope (with and without window)
3. Name card
4. Powerpoint presentation template
5. CD label
6. Small memo / with compliments card

Contact details:

Company name:
PT Varo Ingredients

Address:
Ruko Melati Sentosa Utara, Blok K07 no: 15-16
Duren Sawit Selatan, 13470
Indonesia

Tel:+62 21 738 2906
Fax:+62 21 738 2907
Email: info@varo-ingredients.co.id
Website: www.varo-ingredients.co.id

```html
<!DOCTYPE html>
<html lang="en">
<head>
<meta charset="utf-8">
<title>Varo Ingredients – Letterhead</title>
<link rel="stylesheet" href="https://fonts.googleapis.com/css2?family=Source+Sans+3:wght@400;600&display=swap">
<style>
  :root {
    --backdrop: #e6e6e6;
    --paper: #ffffff;
    --brand-red: #c8242f;
    --brand-blue: #1273bb;
    --brand-orange: #f5a623;
    --label-blue: #1a6fba;
    --ink: #1b1b1b;
  }
  * { box-sizing: border-box; margin: 0; padding: 0; }
  html, body { width: 839px; height: 1200px; overflow: hidden; }
  body {
    background: var(--backdrop);
    font-family: "Source Sans 3", sans-serif;
    color: var(--ink);
    position: relative;
  }
  .letterhead {
    position: absolute;
    left: 36px; top: 28px;
    width: 760px; height: 1076px;
    background: var(--paper);
  }
  .company-name {
    position: absolute;
    left: 268px; top: 48px;
    font-size: 22px; font-weight: 400;
    line-height: 26px;
    color: var(--ink);
  }
  .header-rule {
    position: absolute;
    left: 264px; top: 90px;
    width: 496px; height: 3px;
    display: flex;
  }
  .header-rule .accent { width: 184px; background: var(--brand-orange); }
  .header-rule .main { flex: 1; background: var(--brand-blue); }
  .contact {
    position: absolute;
    left: 76px; top: 160px;
    font-size: 12.6px; line-height: 15.6px;
  }
  .contact dt { color: var(--label-blue); font-weight: 600; }
  .contact dd { margin-bottom: 15px; }
  .letter-body {
    position: absolute;
    left: 268px; width: 460px;
    font-size: 12.6px; line-height: 15.6px;
    text-align: justify;
    hyphens: auto;
  }
  .salutation { top: 159px; }
  .p1 { top: 182px; }
  .p2 { top: 240px; }
  .p3 { top: 350px; }
  .p4 { top: 482px; }
  .closing { top: 614px; }
  .signatory { top: 721px; }
  .footer-band {
    position: absolute;
    left: 264px; bottom: 0;
    width: 496px; height: 52px;
    display: flex;
  }
  .footer-band .accent { width: 84px; background: var(--brand-red); }
  .footer-band .main { flex: 1; background: var(--brand-blue); }
</style>
</head>
<body>
  <main class="letterhead">
    <header>
      <div class="company-name">Varo Ingredients</div>
      <div class="header-rule"><span class="accent"></span><span class="main"></span></div>
    </header>

    <dl class="contact">
      <dt>Address:</dt>
      <dd>Ruko Melati Sentosa Utara,<br>Blok K07 no: 15-16<br>Duren Sawit Selatan, 13470<br>Indonesia.</dd>
      <dt>Phone:</dt>
      <dd>Tel:+62 21 738 2906<br>Fax:+62 21 738 2907</dd>
      <dt>Web/E-mail:</dt>
      <dd>www.varo-ingredients.co.id<br>info@varo-ingredients.co.id</dd>
    </dl>

    <p class="letter-body salutation">Dear (Name),</p>
    <p class="letter-body p1">Lorem Ipsum is simply dummy text of the printing and typesetting industry. Lorem Ipsum has been the industry's standard dummy text ever since the 1500s, when an unknown printer took a galley of type and scrambled.</p>
    <p class="letter-body p2">It to make a type specimen book. It has survived not only five centuries, but also the leap into electronic typesetting, remaining essentially unchanged. It was popularised in the 1960s with the release of Typeline sheets containing Lorem Ipsum passages, and more recently with desktop publishing software like Quillmark PageSetter including versions of Lorem Ipsum.</p>
    <p class="letter-body p3">It is a long established fact that a reader will be distracted by the readable content of a page when looking at its layout. The point of using Lorem Ipsum is that it has a more-or-less normal distribution of letters, as opposed to using 'Content here, content here', making it look like readable English. Many desktop publishing packages and web page editors now use Lorem Ipsum as their default model text, and a search for 'lorem ipsum' will uncover many web sites still in their infancy. Various versions have evolved over the years, sometimes by accident, sometimes on purpose (injected humour and the like).</p>
    <p class="letter-body p4">Contrary to popular belief, Lorem Ipsum is not simply random text. It has roots in a piece of classical Latin literature from 45 BC, making it over 2000 years old. Edwin Harlowe, a Latin professor at Ashford-Lane College in Virginia, looked up one of the more obscure Latin words, consectetur, from a Lorem Ipsum passage.</p>
    <p class="letter-body closing">Sincerely yours,</p>
    <p class="letter-body signatory">Lorem Ipsum<br>Post Title</p>

    <footer class="footer-band"><span class="accent"></span><span class="main"></span></footer>
  </main>
</body>
</html>
```